Organic skincare label - minimalist, earthy, luxe design needed!

I need a label design for a luxury natural skin care line called "Velka Botaniq". Velka means 'earth' in Swahili. I would like the design to embody an earthy feel but be minimalistic and give a luxe vibe. My first product will be a Saffron and Moringa Polish.

The size of the jar is 8oz, label dimensions should be (1.625" Tall x 8.5" Wide)
I will be making other products too such as; oils + toners so I feel free to do labels for glass bottles and/or spray bottles as well.

Forest green, light pinks/nudes/beige, grey, white, gold, are colors that can be used (not all have to be used).

I have included pictures of some things I've worked on myself as well as my original logo design but I need to simplify the logo, no circle around it.
Feel free to get creative.

Thank you! :)
Updates

Target Market(s)

Socially Conscious, Beauty Enthusiast, Minimalist

Industry/Entity Type

Skin Care

Font styles to use
Sans Serif
Other font styles liked:
• "Wonderlove doodle" is the font used for "Velka" in the logo. Feel free to use that or change it as you see fit.

Requirements
Must have
• Simplistic design
would like to stick to a font close to the ones in the logo. Either the one used for the name "Velka" OR the one that the slogan "earth's elixirs" uses.

I have also included some pictures to capture the aesthetic of my social media and website.

Gender neutral

```html
<!DOCTYPE html>
<html lang="en">
<head>
<meta charset="utf-8">
<title>Velka Botaniq – Saffron &amp; Moringa Polish label</title>
<link rel="stylesheet" href="https://fonts.googleapis.com/css2?family=Cormorant+Garamond:ital,wght@0,400;1,400&family=Montserrat:wght@400&display=swap">
<style>
  :root {
    --blush: #d6b8b0;
    --clay: #c8a89b;
    --shell: #e6d5d0;
    --cocoa: #ab8272;
    --cream: #f6f0ee;
    --ink-soft: #a77f70;
    --veil: rgba(255, 255, 255, 0.16);
  }
  * { margin: 0; padding: 0; box-sizing: border-box; }
  html, body {
    width: 1200px;
    height: 230px;
    overflow: hidden;
    background: var(--blush);
  }
  .label {
    position: relative;
    width: 1200px;
    height: 230px;
    overflow: hidden;
    background: var(--blush);
  }
  .label__backdrop {
    position: absolute;
    inset: 0;
    width: 100%;
    height: 100%;
  }
  .backdrop__clay { fill: var(--clay); }
  .backdrop__shell { fill: var(--shell); }

  .flourish {
    position: absolute;
    border-radius: 50%;
  }
  .flourish--left {
    left: 40px;
    top: -20px;
    width: 52px;
    height: 270px;
    background: radial-gradient(ellipse at center, var(--veil) 0%, rgba(255,255,255,0) 70%);
  }
  .flourish--top {
    left: 780px;
    top: -40px;
    width: 310px;
    height: 160px;
    background: radial-gradient(ellipse at center, var(--veil) 0%, rgba(255,255,255,0) 70%);
  }
  .flourish--corner {
    left: 1020px;
    top: 95px;
    width: 200px;
    height: 150px;
    background: radial-gradient(ellipse at center, var(--veil) 0%, rgba(255,255,255,0) 70%);
  }

  .brand-name {
    position: absolute;
    left: 132px;
    top: 72px;
    font-family: "Cormorant Garamond", serif;
    font-weight: 400;
    font-size: 66px;
    line-height: 1;
    color: var(--cream);
    letter-spacing: 0.5px;
    white-space: nowrap;
  }
  .product {
    position: absolute;
    left: 699px;
    top: 76px;
    width: 206px;
    text-align: center;
  }
  .product__title {
    font-family: "Cormorant Garamond", serif;
    font-style: italic;
    font-weight: 400;
    font-size: 31px;
    line-height: 1;
    color: var(--cream);
    white-space: nowrap;
  }
  .product__type {
    margin-top: 9px;
    height: 36px;
    background: var(--cocoa);
    display: flex;
    align-items: center;
    justify-content: center;
    font-family: "Montserrat", sans-serif;
    font-weight: 400;
    font-size: 17px;
    letter-spacing: 4px;
    color: var(--cream);
    padding-left: 4px;
  }
  .net-weight {
    position: absolute;
    left: 1133px;
    top: 184px;
    font-family: "Montserrat", sans-serif;
    font-size: 13px;
    letter-spacing: 2px;
    color: var(--ink-soft);
  }
</style>
</head>
<body>
  <main class="label">
    <svg class="label__backdrop" viewBox="0 0 2550 488" preserveAspectRatio="none" aria-hidden="true">
      <path class="backdrop__clay" d="M970,488 C1050,380 1150,300 1300,230 C1400,170 1440,60 1470,0 L2440,0 C2380,120 2250,170 2100,240 C1980,300 1960,420 1920,488 Z"/>
      <path class="backdrop__shell" d="M1920,488 C1960,420 1980,300 2100,240 C2250,170 2380,120 2440,0 L2550,0 L2550,488 Z"/>
    </svg>

    <div class="flourish flourish--left" role="img" aria-label="Area for a hand-drawn white line flourish running down the left edge"></div>
    <div class="flourish flourish--top" role="img" aria-label="Area for a hand-drawn white leaf-like line flourish at the top right"></div>
    <div class="flourish flourish--corner" role="img" aria-label="Area for a hand-drawn white sweeping line flourish in the lower right corner"></div>

    <h1 class="brand-name">Velka Botaniq</h1>

    <section class="product">
      <p class="product__title">Saffron &amp; Moringa</p>
      <p class="product__type">POLISH</p>
    </section>

    <p class="net-weight">8oz</p>
  </main>
</body>
</html>
```